ONLINE MATTRESS COMPANY REQUIRING BOX DESIGN FOR MATTRESS IN A BOX

WE NEED A BOX DESIGN FOR A NEW COMPANY THAT SELLS A MATTRESS IN A BOX (SIMILAR TO VELNOR.COM) THAT INCORPORATES ONLY 2 COLOURS (TEAL & BLACK) THE BASE COLOUR OF BOX IS WHITE. THE DESIGN HAS TO INSPIRE MILLENNIAL AND YOUNG SHOPPERS TO WANT TO PURCHASE THE PRODUCT. BOX SHOULD BE SIMPLE AND CLEAN. ONE SIDE HAS TO SHOW THE OPENING INSTRUCTIONS WHICH ARE ATTACHED IN A SAMPLE BOX.

Target Market(s)

MILLENNIALS

Industry/Entity Type

Furniture Store

Font styles to use
Serif
Sans Serif

Colors
ffffff
33b8a4

Requirements
Must have
• ONE SIDE MUST HAVE OPEN INSTRUCTIONS (SEE EXAMPLE); THE FACTORY CAN ONLY PRING ON A WHITE BOX WITH 2 COLOURS. THE WRITING AND SHAPES CAN BE TEAL AND BLACK BUT THE WHOLE BOX CANNOT BE TEAL AND BLACK, JUST THE ART WORK.
Should not have
• CAN ONLY BE 2 COLOURS; BOX COLOUR IS WHITE ; TEAL & BLACK AS OTHER INK COLOURS.

SHOULD NOT SHOW LOGO VERTICALLY (UP AND DOWN) BECAUSE IT IS HARD TO READ, SHOULD BE HORIZONTAL.

DO NOT SHOW MATTRESS OR PILLOW ON BOX IT'S ONLY TO HELP GUIDE YOU SO KNOW WHAT THE PRODUCT IS!

```html
<!DOCTYPE html>
<html lang="en">
<head>
<meta charset="utf-8">
<title>Nuvelo Mattress Box</title>
<link href="https://fonts.googleapis.com/css2?family=Poppins:wght@300;400;500;600;800&display=swap" rel="stylesheet">
<style>
  :root {
    --teal: #10b9b3;
    --white: #ffffff;
    --ink: #111111;
    --fold: #e8957a;
    --teal-soft: #bfe9e7;
    --grey-soft: #e4e4e4;
  }
  html, body { margin: 0; padding: 0; overflow: hidden; }
  body { width: 1200px; height: 1067px; background: var(--white); font-family: "Poppins", sans-serif; }
  .canvas { position: relative; width: 1200px; height: 1067px; overflow: hidden; }
  .dieline { position: absolute; left: 0; top: 0; }
  .brand-small {
    position: absolute; left: 148px; top: 196px; margin: 0;
    font-size: 56px; font-weight: 500; color: var(--teal); line-height: 1; letter-spacing: -1px;
  }
  .tagline {
    position: absolute; right: 869px; margin: 0; font-weight: 300;
    font-size: 18px; color: var(--teal); line-height: 1; white-space: nowrap;
  }
  .tagline.first { top: 289px; }
  .tagline.second { top: 320px; }
  .product-title {
    position: absolute; left: 380px; top: 523px; margin: 0;
    font-size: 21px; font-weight: 600; color: var(--ink); line-height: 1;
  }
  .brand-large {
    position: absolute; left: 374px; top: 528px; margin: 0;
    font-size: 126px; font-weight: 500; color: var(--teal); line-height: 1; letter-spacing: -3px;
  }
  .care-icons { position: absolute; left: 137px; top: 882px; display: flex; gap: 3px; }
  .care-icon { width: 20px; height: 20px; border: 1.5px solid var(--teal); box-sizing: border-box; }
  .steps { position: absolute; right: 152px; top: 0; width: 170px; }
  .step { position: absolute; right: 0; width: 170px; text-align: right; }
  .step-badge {
    position: absolute; right: 0; top: 0; width: 86px; height: 86px;
    background: var(--teal); border-radius: 50% 50% 0 50%;
  }
  .step-art {
    position: absolute; left: 18px; top: 18px; width: 50px; height: 50px;
    border-radius: 8px; background: linear-gradient(135deg, #ffffff, #d8f3f2);
  }
  .step-title { position: absolute; right: 0; top: 90px; margin: 0; font-size: 18px; font-weight: 800; line-height: 1; color: var(--teal); white-space: nowrap; }
  .step-text { position: absolute; right: 0; top: 114px; margin: 0; font-size: 9px; line-height: 11.3px; color: var(--ink); white-space: nowrap; }
  .recycle-note { position: absolute; right: 152px; top: 917px; margin: 0; font-size: 9px; line-height: 11.3px; color: var(--ink); text-align: right; white-space: nowrap; }
</style>
</head>
<body>
<main class="canvas">
  <svg class="dieline" width="1200" height="1067" viewBox="0 0 1200 1067">
    <defs>
      <clipPath id="box-area"><rect x="120" y="106" width="960" height="854"/></clipPath>
    </defs>
    <rect x="120" y="106" width="960" height="854" fill="var(--white)"/>
    <g clip-path="url(#box-area)">
      <path d="M849.6 960 V648 A324 324 0 1 0 525.6 972" fill="none" stroke="var(--teal)" stroke-width="24"/>
      <path d="M869.6 960 V648 A344 344 0 1 0 525.6 992" fill="none" stroke="var(--teal)" stroke-width="2"/>
      <line x1="120" y1="314" x2="326" y2="314" stroke="var(--teal)" stroke-width="1.5"/>
    </g>
    <rect x="402" y="114" width="158" height="142" fill="var(--teal-soft)" role="img" aria-label="Dot grid texture"/>
    <rect x="638" y="814" width="159" height="142" fill="var(--grey-soft)" role="img" aria-label="Dot grid texture"/>
    <g stroke="var(--fold)" stroke-width="1">
      <line x1="360" y1="106" x2="360" y2="960"/>
      <line x1="600" y1="106" x2="600" y2="960"/>
      <line x1="840" y1="106" x2="840" y2="960"/>
    </g>
    <rect x="120" y="106" width="960" height="854" fill="none" stroke="var(--fold)" stroke-width="1"/>
    <g fill="none" stroke="var(--teal)" stroke-width="1.8" transform="translate(1037 901)">
      <path d="M-6 4 L0 -6 L6 4 Z"/>
    </g>
  </svg>

  <p class="brand-small">nuvelo</p>
  <p class="tagline first">Better Sleep For</p>
  <p class="tagline second">A Better Tommorrow</p>

  <p class="product-title">The Nuvelo Mattress</p>
  <p class="brand-large">nuvelo</p>

  <div class="care-icons" aria-label="Handling marks">
    <span class="care-icon"></span><span class="care-icon"></span><span class="care-icon"></span>
  </div>

  <section class="steps">
    <div class="step" style="top:148px">
      <div class="step-badge"><div class="step-art" role="img" aria-label="Open box with rolled mattress"></div></div>
      <h3 class="step-title">Unbox</h3>
      <p class="step-text">Open the box<br>from the top and lay it on it's side<br>to pull out the mattress</p>
    </div>
    <div class="step" style="top:328px">
      <div class="step-badge"><div class="step-art" role="img" aria-label="Mattress unrolling"></div></div>
      <h3 class="step-title">Position &amp; Unfold</h3>
      <p class="step-text">Now it's time<br>to unwrap and unfold<br>your 'NUVELO' mattress.</p>
    </div>
    <div class="step" style="top:508px">
      <div class="step-badge"><div class="step-art" role="img" aria-label="Mattress expanding with clock"></div></div>
      <h3 class="step-title">Expansion</h3>
      <p class="step-text">'NUVELO' can be used 2-4 hours after<br>opening but may need 24-48 hours<br>for optimum expansion &amp; comfort.</p>
    </div>
    <div class="step" style="top:687px">
      <div class="step-badge"><div class="step-art" role="img" aria-label="Person sleeping on mattress"></div></div>
      <h3 class="step-title">Relax</h3>
      <p class="step-text">Open the box<br>from the top and lay it on it's side<br>to pull out the mattress</p>
    </div>
  </section>

  <p class="recycle-note">Recycle the box and<br>do youe little bit for the planet</p>
</main>
</body>
</html>
```